Frostwyn.co - Polar Expeditions Specialists

We need a modern, visually striking business card for Frostwyn.co, a company specialized in selling expedition cruises to the most remote regions on Earth, with a focus on the Arctic and Antarctica. The design should instantly communicate that the cardholder is an expert in polar travel. Use clean, premium aesthetics with cool tones like icy blue and white, possibly incorporating polar imagery (ice, glaciers, penguins, etc.)

Attached the logo

Contact Information for Business Card

Feels high-end and trustworthy.. Visually memorable — encourages people to keep it

Colors
0054AA
0677BA
7BADD7
CADEEF
E8F1F8

Requirements
Must have
• ice, glaciers, penguins, montains
Nice to have
• modern, transparente,

```html
<!DOCTYPE html>
<html lang="en">
<head>
<meta charset="utf-8">
<title>Frostwyn.co – Business Card</title>
<link href="https://fonts.googleapis.com/css2?family=Poppins:wght@400;500;600;700&display=swap" rel="stylesheet">
<style>
  :root {
    --brand-blue: #3478b9;
    --card-white: #ffffff;
    --ink: #2b2b2b;
    --divider: #c9c9c9;
    --backdrop: #858585;
  }
  * { margin: 0; padding: 0; box-sizing: border-box; }
  html, body {
    width: 1093px; height: 1200px; overflow: hidden;
    background: var(--backdrop);
    font-family: "Poppins", sans-serif;
  }
  .canvas { position: relative; width: 1093px; height: 1200px; }

  .card {
    position: absolute; left: 265px; width: 578px; height: 356px;
    border-radius: 24px; overflow: hidden;
  }
  .card--front { top: 226px; background: var(--card-white); }
  .card--back { top: 621px; background: var(--brand-blue); }

  .front__band {
    position: absolute; left: 0; right: 0; bottom: 0; height: 9px;
    background: var(--brand-blue);
  }

  .brand { position: absolute; text-align: center; line-height: 1; }
  .brand__mark {
    display: block; margin: 0 auto; border-radius: 50%;
  }
  .brand__name { display: block; font-weight: 700; letter-spacing: -0.5px; }
  .brand__tagline { display: block; font-weight: 500; }

  .card--front .brand { left: 20px; width: 270px; top: 104px; color: var(--brand-blue); }
  .card--front .brand__mark { width: 70px; height: 70px; background: var(--brand-blue); margin-bottom: 22px; }
  .card--front .brand__name { font-size: 38px; }
  .card--front .brand__tagline { font-size: 13px; margin-top: 12px; }

  .card--back .brand { left: 0; width: 100%; top: 88px; color: var(--card-white); }
  .card--back .brand__mark { width: 86px; height: 86px; background: var(--card-white); margin-bottom: 28px; }
  .card--back .brand__name { font-size: 52px; }
  .card--back .brand__tagline { font-size: 17px; margin-top: 14px; letter-spacing: 0.2px; }

  .front__divider {
    position: absolute; left: 288px; top: 74px; width: 1.5px; height: 209px;
    background: linear-gradient(to bottom, transparent, var(--divider) 15%, var(--divider) 85%, transparent);
  }

  .contact { position: absolute; left: 311px; top: 88px; color: var(--ink); }
  .contact__name { font-size: 24px; font-weight: 600; color: var(--brand-blue); line-height: 1.05; }
  .contact__role { font-size: 17px; line-height: 1.1; }
  .contact__list { list-style: none; margin-top: 16px; }
  .contact__item {
    display: flex; align-items: center; gap: 7px;
    font-size: 17px; line-height: 21px;
  }
  .contact__icon { width: 16px; height: 16px; flex: none; fill: var(--brand-blue); }
  .contact__accent { color: var(--brand-blue); }
  .contact__address { font-size: 17px; line-height: 21px; margin-top: 12px; }
</style>
</head>
<body>
<main class="canvas">
  <section class="card card--front" aria-label="Business card front">
    <div class="brand">
      <span class="brand__mark" aria-hidden="true"></span>
      <span class="brand__name">Frostwyn.co</span>
      <span class="brand__tagline">Polar Expeditions Specialists</span>
    </div>

    <div class="front__divider"></div>

    <div class="contact">
      <p class="contact__name">Elias Marren</p>
      <p class="contact__role">Managing Director</p>
      <ul class="contact__list">
        <li class="contact__item">
          <svg class="contact__icon" viewBox="0 0 24 24" aria-hidden="true"><path d="M6.6 10.8a15.1 15.1 0 0 0 6.6 6.6l2.2-2.2c.3-.3.7-.4 1-.2 1.1.4 2.3.6 3.6.6.6 0 1 .4 1 1V20c0 .6-.4 1-1 1A17 17 0 0 1 3 4c0-.6.4-1 1-1h3.5c.6 0 1 .4 1 1 0 1.3.2 2.5.6 3.6.1.3 0 .7-.2 1z"/></svg>
          055-210 387 614
        </li>
        <li class="contact__item">
          <svg class="contact__icon" viewBox="0 0 24 24" aria-hidden="true"><path d="M2 5h20v14H2z M4 7v.4l8 5.3 8-5.3V7z" fill-rule="evenodd"/></svg>
          hello@mailsite.com
        </li>
        <li class="contact__item">
          <svg class="contact__icon" viewBox="0 0 24 24" aria-hidden="true"><path d="M12 2a10 10 0 1 0 0 20 10 10 0 0 0 0-20zm6.9 9h-3a15 15 0 0 0-1.3-6A8 8 0 0 1 18.9 11zM12 4c.9 1.2 1.8 3.6 2 7h-4c.2-3.4 1.1-5.8 2-7zM9.4 5a15 15 0 0 0-1.3 6h-3A8 8 0 0 1 9.4 5zM5.1 13h3a15 15 0 0 0 1.3 6 8 8 0 0 1-4.3-6zM12 20c-.9-1.2-1.8-3.6-2-7h4c-.2 3.4-1.1 5.8-2 7zm2.6-1a15 15 0 0 0 1.3-6h3a8 8 0 0 1-4.3 6z"/></svg>
          <span>www.<span class="contact__accent">sitedomain</span>.com</span>
        </li>
      </ul>
      <p class="contact__address">421, Address line goes here<br>45452,Country Name</p>
    </div>

    <div class="front__band"></div>
  </section>

  <section class="card card--back" aria-label="Business card back">
    <div class="brand">
      <span class="brand__mark" aria-hidden="true"></span>
      <span class="brand__name">Frostwyn.co</span>
      <span class="brand__tagline">Polar Expeditions Specialists</span>
    </div>
  </section>
</main>
</body>
</html>
```